Medical Billing Business needs a web page designed

We need a web page for a new medical billing business for prospective clients to go to to get information about our company. It needs to show what our company stands for and our billing rates. Our colors are blue, gray and white. I have attached our logo, brochure and mission statement.

Need tabs at top for "about us", "contact us" "specials". On contact page, need a form to fill out that will be automatically emailed to us upon completion. Under specials...Sign a contract by the end of August 2014 and receive one month of billing FREE. ***Receive 25% off the first 4 months of the contract***

```html
<!DOCTYPE html>
<html lang="en">
<head>
<meta charset="utf-8">
<title>Prairie Claims Billing, LLC</title>
<link href="https://fonts.googleapis.com/css2?family=Cinzel:wght@400;600&family=Open+Sans:wght@300;400&family=Arimo:wght@400;700&display=swap" rel="stylesheet">
<style>
:root{
  --brand-blue:#0b5a82;
  --brand-blue-dark:#094a6b;
  --band-gray:#d9d9d9;
  --footer-gray:#d6d6d6;
  --row-gray:#e4e4e4;
  --row-gray-alt:#dadada;
  --text-dark:#333;
  --text-mid:#444;
  --accent-orange:#ef8a1c;
  --white:#fff;
}
*{margin:0;padding:0;box-sizing:border-box}
html,body{width:1200px;height:2239px;overflow:hidden;background:var(--white)}
body{position:relative;font-family:"Open Sans",Arial,sans-serif;color:var(--text-dark)}

/* Header */
.site-header{position:absolute;left:0;top:0;width:1200px;height:78px;background:var(--brand-blue)}
.main-nav a{position:absolute;top:30px;font-family:"Cinzel",serif;font-size:21px;color:var(--white);text-decoration:none;letter-spacing:.5px}
.logo-tab{position:absolute;left:495px;top:0;width:210px;height:136px}
.logo-name{position:absolute;left:497px;width:207px;top:72px;text-align:center;font-family:"Cinzel",serif;font-size:16px;font-weight:600;color:var(--brand-blue);letter-spacing:2px;line-height:1.3}
.logo-dot{position:absolute;left:581px;top:14px;width:38px;height:38px;background:var(--brand-blue);border-radius:50%}

/* Hero */
.hero-photo{position:absolute;left:187px;top:134px;width:783px;height:445px;background:linear-gradient(180deg,#fbfbfb 0%,#eef2f5 55%,#e2e8ee 100%)}

/* Mission band */
.mission-band{position:absolute;left:0;top:579px;width:1200px;height:222px;background:var(--band-gray)}
.mission-title{position:absolute;left:0;width:1200px;top:618px;text-align:center;font-weight:300;font-size:36px;line-height:44px;color:var(--text-mid)}
.mission-text{position:absolute;left:128px;width:944px;top:673px;text-align:center;font-size:13.8px;line-height:17.2px;color:var(--text-mid)}

/* Services section */
.hipaa-title{position:absolute;left:128px;top:885px;font-family:"Arimo",Arial,sans-serif;font-weight:400;font-size:20px;color:var(--text-dark)}
.hipaa-text{position:absolute;left:128px;top:914px;width:540px;font-family:"Arimo",Arial,sans-serif;font-size:13.8px;line-height:16.6px;color:var(--text-dark)}
.divider{position:absolute;left:128px;top:1031px;width:499px;border-top:2px dotted #888}
.fee-badge{position:absolute;left:128px;top:1049px;width:114px;height:123px;background:var(--accent-orange);border-radius:8px}
.collection-head{position:absolute;left:264px;top:1054px;font-family:"Arimo",Arial,sans-serif;font-weight:700;font-size:28px;line-height:36px;color:#3c3c3c;letter-spacing:.2px}
.collection-head .hl{color:var(--brand-blue)}
.rates-title{position:absolute;left:124px;top:1264px;font-size:29px;line-height:34px;color:var(--brand-blue);font-weight:400}
.rates-table{position:absolute;left:122px;top:1358px;width:415px;border-collapse:collapse;font-family:"Arimo",Arial,sans-serif}
.rates-table th{background:var(--brand-blue);color:var(--white);font-weight:400;font-size:14px;text-align:left;height:36px;padding-left:21px}
.rates-table td{font-size:13.5px;color:#444;height:30px;padding-left:21px;border-top:1px solid #fff;background:var(--row-gray)}
.rates-table tr:nth-child(even) td{background:var(--row-gray-alt)}
.rates-note{position:absolute;left:124px;top:1506px;width:430px;font-family:"Arimo",Arial,sans-serif;font-size:11.5px;line-height:15px;color:#333}
.rates-phone{position:absolute;left:123px;top:1541px;font-family:"Arimo",Arial,sans-serif;font-size:24px;color:var(--accent-orange)}
.rates-address{position:absolute;left:124px;top:1570px;font-family:"Arimo",Arial,sans-serif;font-size:14px;color:#333}
.doctor-photo{position:absolute;left:590px;top:873px;width:500px;height:769px;background:linear-gradient(180deg,#f3f0ec 0%,#f4f6f8 45%,#e6ebf0 100%);border-radius:220px 220px 0 0}

/* Features band */
.features{position:absolute;left:0;top:1642px;width:1200px;height:462px;background:var(--brand-blue)}
.features-title{position:absolute;left:124px;top:1684px;font-weight:300;font-size:31px;color:var(--white)}
.features-text{position:absolute;left:124px;top:1734px;width:955px;font-size:14px;line-height:17.5px;color:#dbe7ee}
.feature-list{position:absolute;list-style:none;font-size:14px;color:#dbe7ee;line-height:17px}
.feature-list li{position:relative;padding-left:27px;margin-bottom:13px}
.feature-list li svg{position:absolute;left:0;top:0;width:17px;height:15px}
.feature-list.left{left:130px;top:1822px;width:470px}
.feature-list.right{left:622px;top:1822px;width:470px}

/* Footer */
.site-footer{position:absolute;left:0;top:2104px;width:1200px;height:135px;background:var(--footer-gray)}
.footer-dot{position:absolute;left:176px;top:2132px;width:36px;height:36px;border-radius:50%;background:var(--brand-blue)}
.footer-name{position:absolute;left:120px;width:148px;top:2176px;text-align:center;font-family:"Cinzel",serif;font-size:13px;font-weight:600;color:var(--brand-blue);letter-spacing:1.5px;line-height:1.35}
.footer-nav{position:absolute;left:428px;top:2172px;font-family:"Cinzel",serif;font-size:16px}
.footer-nav a{color:var(--brand-blue);text-decoration:none;margin-right:10px}
.footer-phone{position:absolute;left:894px;top:2140px;font-family:"Arimo",Arial,sans-serif;font-size:24px;color:var(--brand-blue-dark)}
.footer-address{position:absolute;left:896px;top:2172px;font-family:"Arimo",Arial,sans-serif;font-size:14px;color:var(--brand-blue-dark)}
.social-dots{position:absolute;left:896px;top:2195px;display:flex;gap:6px}
.social-dots span{width:11px;height:11px;border-radius:50%;background:var(--brand-blue-dark)}
</style>
</head>
<body>

<header class="site-header">
  <nav class="main-nav">
    <a href="#" style="left:185px">HOME</a>
    <a href="#" style="left:299px">ABOUT US</a>
    <a href="#" style="left:775px">SPECIALS</a>
    <a href="#" style="left:913px">CONTACT</a>
  </nav>
</header>
<svg class="logo-tab" viewBox="0 0 210 136" aria-hidden="true">
  <path d="M2 0 V40 C2 95 50 134 105 134 C160 134 208 95 208 40 V0 Z" fill="#fff" stroke="#0b5a82" stroke-width="2"/>
</svg>
<span class="logo-dot"></span>
<div class="logo-name">PRAIRIE CLAIMS</div>

<div class="hero-photo" role="img" aria-label="Photo of a smiling team of five doctors in white coats giving thumbs up"></div>

<section class="mission-band"></section>
<h1 class="mission-title">QUICK, COST EFFICIENT SOLUTION FOR YOUR PRACTICE</h1>
<p class="mission-text">Our mission at Prairie Claims Billing, LLC is to set the standard of excellence for providing quality medical administrative services to our clients.&nbsp; Our company's success, which is characterized by organizationalexcellence as well as our responsiveness of our client's needs, has been founded on our customer service.&nbsp; Our clients and their patients will trust Prairie Claims Billing, LLC to do everything that we commit to and beyond.&nbsp; By providing the quality services that they expect and deserve, Prairie Claims Billing, LLC strives to be the preferred company for every physicians' needs.</p>

<div class="doctor-photo" role="img" aria-label="Photo of a smiling female doctor with a stethoscope holding out an open hand"></div>

<h2 class="hipaa-title">HIPAA Compliant</h2>
<p class="hipaa-text">We know the importance of your patients' information security. We maintain and protect that information by following all HIPAa laws and regulations to the fullest. Our security measures make sure that only authorized users have the information needed to fulfill their job duties while protecting unauthorized use of information. Our state of the art documentation storage system, DocVault, is 100% HIPAA compliant</p>
<div class="divider"></div>

<div class="fee-badge" role="img" aria-label="Badge: no start-up fees"></div>
<h2 class="collection-head">ENHANCE AND<br><span class="hl">IMPROVE</span> YOUR<br>COLLECTION RATE</h2>

<h2 class="rates-title">OUR BILLING SERVICES START<br>AS LOW AS 5% AND 6%</h2>
<table class="rates-table">
  <tr><th>Billing Services</th><th>Billing and Coding Services</th></tr>
  <tr><td>$150,001 &lt; --5%</td><td>$150,001 &lt; --6%</td></tr>
  <tr><td>$100,001-$150,000 --5%</td><td>$100,001-$150,000 --6.5%</td></tr>
  <tr><td>$80,001-$100,000 --5.75%</td><td>$80,001-$100,000 --6.75%</td></tr>
</table>
<p class="rates-note">Please contact us to make an appointment for all of your medical billing and/or coding needs.</p>
<div class="rates-phone">(866) 555-0142</div>
<div class="rates-address">418 N Elm Street, Dalton, KS 66700</div>

<section class="features"></section>
<h2 class="features-title">Featues and Advantages</h2>
<p class="features-text">Prairie Claims Billing, LLC is a full service Practice Managment Company. We are dedicated to providing your practice with the highest quality of professional service. In the ever-changing regulations of the medical insurance industry, we understand the challenges that face many medical practices today.</p>

<ul class="feature-list left">
  <li><svg viewBox="0 0 18 16"><path d="M1 9 L6 14 L17 2" fill="none" stroke="#fff" stroke-width="3"/></svg>Staff is certified by the NCCB in the Billing and Coding (ICD-9-CM)</li>
  <li><svg viewBox="0 0 18 16"><path d="M1 9 L6 14 L17 2" fill="none" stroke="#fff" stroke-width="3"/></svg>Extensive training with ICD-10 (Mandatory codes effective<br>Octerber 2015)</li>
  <li><svg viewBox="0 0 18 16"><path d="M1 9 L6 14 L17 2" fill="none" stroke="#fff" stroke-width="3"/></svg>Claims submission in 24 hours or less</li>
  <li><svg viewBox="0 0 18 16"><path d="M1 9 L6 14 L17 2" fill="none" stroke="#fff" stroke-width="3"/></svg>Reduce denial/rejection rate with claim scrubbing</li>
  <li><svg viewBox="0 0 18 16"><path d="M1 9 L6 14 L17 2" fill="none" stroke="#fff" stroke-width="3"/></svg>Electronic and Paper claim submission</li>
  <li><svg viewBox="0 0 18 16"><path d="M1 9 L6 14 L17 2" fill="none" stroke="#fff" stroke-width="3"/></svg>Increase revenue with aggressive insurance follow-up</li>
  <li><svg viewBox="0 0 18 16"><path d="M1 9 L6 14 L17 2" fill="none" stroke="#fff" stroke-width="3"/></svg>Insurance appeal lettersa dn follow-up</li>
</ul>
<ul class="feature-list right">
  <li><svg viewBox="0 0 18 16"><path d="M1 9 L6 14 L17 2" fill="none" stroke="#fff" stroke-width="3"/></svg>No equipment purchase</li>
  <li><svg viewBox="0 0 18 16"><path d="M1 9 L6 14 L17 2" fill="none" stroke="#fff" stroke-width="3"/></svg>Increase practice profitability</li>
  <li><svg viewBox="0 0 18 16"><path d="M1 9 L6 14 L17 2" fill="none" stroke="#fff" stroke-width="3"/></svg>Montly patient billing and patient balance follow-up</li>
  <li><svg viewBox="0 0 18 16"><path d="M1 9 L6 14 L17 2" fill="none" stroke="#fff" stroke-width="3"/></svg>Payment posting</li>
  <li><svg viewBox="0 0 18 16"><path d="M1 9 L6 14 L17 2" fill="none" stroke="#fff" stroke-width="3"/></svg>Montly financial reports</li>
  <li><svg viewBox="0 0 18 16"><path d="M1 9 L6 14 L17 2" fill="none" stroke="#fff" stroke-width="3"/></svg>Quarterly Medicare fee updates</li>
</ul>

<footer class="site-footer"></footer>
<span class="footer-dot"></span>
<div class="footer-name">PRAIRIE CLAIMS</div>
<nav class="footer-nav">
  <a href="#">HOME</a><a href="#">ABOUT US</a><a href="#">SPECIALS</a><a href="#">CONTACT US</a>
</nav>
<div class="footer-phone">(866) 555-0142</div>
<div class="footer-address">418 N Elm Street, Dalton, KS 66700</div>
<div class="social-dots" aria-label="Social links"><span></span><span></span><span></span><span></span></div>

</body>
</html>
```